Letterhead design for Dental Practice - Ashby Lane Dental Care

Letterhead for Private Dental Practice. To be used for all official correspondance and for printing treatment details on to be given to patients.

Target Market(s)

Private dental patients

Industry/Entity Type

Dental Clinic

Font styles to use
Other font styles liked:
• nexa-light

Colors
33a6d7
1c66ac
85abd2

Requirements
Must have
• info in the footer and header needs to be 3.5cm from upper/lower boader of paper, see photo in uploaded files
• info details:
• tel. 01632 947 3051
• email info@ashbylanedc.co.uk
• ashbylanedentalcare.co.uk
• 17b Ashby Lane Elmbrook Kessington KS4 7QT
• nexa-light font as in uploaded logo files
Should not have
• No funny tooth pictures

```html
<!DOCTYPE html>
<html lang="en">
<head>
<meta charset="utf-8">
<title>Ashby Lane Dental Care – Letterhead</title>
<link rel="stylesheet" href="https://fonts.googleapis.com/css2?family=Montserrat:wght@300&display=swap">
<style>
  :root {
    --paper: #ffffff;
    --brand-blue: #1c66ac;
    --brand-sky: #33a6d7;
    --watermark: #f6f6f7;
    --footer-ink: #3a4250;
  }
  html, body {
    margin: 0;
    padding: 0;
    overflow: hidden;
    background: var(--paper);
  }
  .letterhead {
    position: relative;
    width: 849px;
    height: 1200px;
    background: var(--paper);
    font-family: "Montserrat", sans-serif;
    font-weight: 300;
    overflow: hidden;
  }
  .brand {
    position: absolute;
    left: 20px;
    top: 86px;
    display: flex;
    align-items: center;
    gap: 10px;
  }
  .brand-dot {
    width: 22px;
    height: 22px;
    border-radius: 50%;
    background: var(--brand-sky);
  }
  .brand-name {
    margin: 0;
    font-size: 26px;
    font-weight: 300;
    color: var(--brand-blue);
    letter-spacing: 0.3px;
    line-height: 1;
    white-space: nowrap;
  }
  .watermark {
    position: absolute;
    left: 243px;
    top: 345px;
    width: 366px;
    height: 495px;
  }
  .contact {
    position: absolute;
    left: 20px;
    bottom: 26px;
    margin: 0;
    font-style: normal;
    font-size: 26px;
    line-height: 33px;
    color: var(--footer-ink);
    letter-spacing: 0.4px;
  }
  .contact span { display: block; white-space: nowrap; }
</style>
</head>
<body>
  <main class="letterhead">
    <header class="brand">
      <span class="brand-dot" aria-hidden="true"></span>
      <h1 class="brand-name">Ashby Lane Dental Care</h1>
    </header>

    <svg class="watermark" viewBox="0 0 366 495" role="img" aria-label="Large faint tooth watermark">
      <rect x="0" y="0" width="366" height="495" rx="150" fill="var(--watermark)"/>
    </svg>

    <address class="contact">
      <span>tel. 01632 947 3051</span>
      <span>email. info@ashbylanedc.co.uk ashbylanedentalcare.co.uk</span>
      <span>17b Ashby Lane Elmbrook Kessington KS4 7QT</span>
    </address>
  </main>
</body>
</html>
```